Luxury Court Grove/academy - Webdesign

We want to develop a cutting edge website for a luxury tennis academy. Academy is based in Russia and includes all the necessary amenities for comfortable stay: apartments, spa, tennis courts, training facilities, etc.
We would like to see a clean, simple and modern design (with implementation of all the current trends in web design, although our project has to be distinct and unique).
Color scheme: we would like to see colors present in our logos and all the current associated with tennis. We are open to your ideas and creativity on this front.
The final design should communicate simplicity, be user friendly and convey premium feel.
We woud like to see unique ideas in the design, unconventional techniques, etc.
We don't want standard template design!
Updates
We want to mention that this Tennis Academy has a light focus on nature, as the new material we have uploaded illustrates.
Additional comment to everyone!
We couldn't upload this file to the system: it is too big.
Thank you everyone for your submissions!
Industry/Entity Type
Training
Requirements
Must have
- We would like to see the designs for the following pages:
Home Page:
- Slideshow
- Short description and all the standard stuff
About Us:
- Description with some images
Services:
- Simple description of all of the provided services and possibility to book all of them on the website
! Important ! Develop small system for booking of the days of stay and registration for the courses
Booking and registration !
News:
- Creative layout to display recent news of the academy
Coaches:
- Image and short description of our staff.
Club / Gallery:
- Images and descriptions of the amenities in the territory.
We want a unique display of images: not just lines and rows filled with images
- One idea: an interactive map that displays images and description on mouseover or click on the object on the map (but again, we are open to all your ideas)
Contacts:
- Contact form, contacts, etc.
Sport Store:
- Basic layout for the goods and services provided by the sports store located in the academy
Prices:
- Price lists and ranges with a button leading to registration and booking
For pages like About Us and Services, it would be enough to develop one unified layout for all of them.

```html
<!DOCTYPE html>
<html lang="en">
<head>
<meta charset="utf-8">
<title>Court Grove – Tennis Academy</title>
<link href="https://fonts.googleapis.com/css2?family=Open+Sans:wght@400;600;700&family=Great+Vibes&display=swap" rel="stylesheet">
<style>
:root{
  --green:#2f8f3a;
  --green-light:#6cb33f;
  --green-dark:#17733a;
  --lime:#8bc53f;
  --ink:#111;
  --muted:#9a9a9a;
  --line:#d9d9d9;
  --paper:#fff;
  --frame:rgba(255,255,255,.82);
}
*{margin:0;padding:0;box-sizing:border-box}
html,body{width:1150px;height:1200px;overflow:hidden}
body{position:relative;font-family:"Open Sans",Arial,sans-serif;background:#7fa35a}
.scenery{position:absolute;inset:0;background:
  radial-gradient(ellipse at 10% 10%,#e8f0df 0,transparent 35%),
  radial-gradient(ellipse at 95% 20%,#f4f8ef 0,transparent 30%),
  linear-gradient(180deg,#9fb98a 0%,#6f9a4a 50%,#8fb04b 75%,#5d8a32 100%)}
.frame{position:absolute;left:96px;top:32px;width:958px;height:1115px;background:var(--frame)}
.page{position:absolute;left:110px;top:45px;width:930px;height:1089px;background:var(--paper);border:1px solid #ddd}
.brand{position:absolute;left:36px;top:48px;display:flex;align-items:center;gap:14px}
.brand-name{font-weight:700;font-size:58px;letter-spacing:-1px;color:var(--green);line-height:1}
.brand-dot{width:56px;height:56px;border-radius:50%;background:var(--lime)}
.contact{position:absolute;right:18px;top:82px;text-align:right;font-size:20px;color:var(--ink);line-height:29px}
.contact div{display:flex;align-items:center;justify-content:flex-end;gap:12px}
.nav{position:absolute;left:0;top:150px;width:928px;height:51px;background:linear-gradient(#6cb33f,#2e8f3a 55%,#17733a);display:flex;align-items:center}
.nav a{color:#fff;text-decoration:none;font-size:14px;padding:0 19px;height:51px;line-height:55px}
.nav a.active{background:linear-gradient(#4c9d3b,#1d7a38);padding:0 25px}
.hero{position:absolute;left:0;top:202px;width:928px;height:403px;background:linear-gradient(180deg,#2e5a23 0%,#5d8d3a 35%,#6fa044 70%,#9b6a5a 96%,#a07060 100%)}
.slides{position:absolute;left:0;top:605px;width:928px;height:105px;display:flex;background:var(--green)}
.arrow{width:44px;height:105px;background:linear-gradient(#6cb33f,#2e8f3a);display:flex;align-items:center;justify-content:center}
.arrow span{width:33px;height:33px;border-radius:50%;background:#fff;display:flex;align-items:center;justify-content:center}
.slide{flex:1;border-left:1px solid #c9e4b8;background:linear-gradient(#6cb33f,#2e8f3a 55%,#17733a);color:#fff;font-size:18px;letter-spacing:.5px;text-transform:uppercase;display:flex;align-items:center;justify-content:center;position:relative;text-shadow:0 1px 2px rgba(0,0,0,.3)}
.slide:first-of-type{border-left:none}
.slide.current::before{content:"";position:absolute;top:0;left:90px;border:10px solid transparent;border-top:16px solid #2e8f3a}
.shadow{position:absolute;left:110px;top:710px;width:720px;height:22px;background:radial-gradient(ellipse at 50% 0,rgba(0,0,0,.85),rgba(0,0,0,0) 70%)}
.welcome{position:absolute;left:0;width:928px;top:762px;text-align:center;font-family:"Great Vibes",cursive;font-size:42px;color:var(--green-dark)}
.intro{position:absolute;left:42px;width:846px;top:835px;text-align:center;font-size:13.5px;line-height:19px;color:var(--muted)}
.divider{position:absolute;top:943px;height:1px;width:290px;background:linear-gradient(90deg,transparent,var(--line))}
.divider.right{right:42px;background:linear-gradient(90deg,var(--line),transparent)}
.divider.left{left:42px}
.read-more{position:absolute;left:385px;top:919px;width:170px;height:45px;border-radius:14px;background:linear-gradient(#6cb33f,#1f7d38);color:#fff;font-size:16px;display:flex;align-items:center;justify-content:center;border:1px solid #1a6e31}
.social{position:absolute;left:0;width:928px;top:993px;display:flex;justify-content:center;gap:12px}
.social span{width:42px;height:42px;border-radius:50%;background:radial-gradient(#fff,#e2e2e2);border:1px solid #ddd}
.copyright{position:absolute;left:0;width:928px;top:1044px;text-align:center;font-size:13.5px;color:var(--ink)}
.copyright a{color:var(--green-dark);text-decoration:none}
</style>
</head>
<body>
<div class="scenery" role="img" aria-label="Sunlit pine trees and meadow grass surrounding the academy"></div>
<div class="frame"></div>
<div class="page">
  <div class="brand"><span class="brand-name">Court Grove</span><span class="brand-dot"></span></div>
  <div class="contact">
    <div><svg width="28" height="22" viewBox="0 0 28 22"><path d="M2 8c0-4 24-4 24 0v3h-6V8H8v3H2z" fill="#111"/><rect x="6" y="11" width="16" height="9" rx="2" fill="#111"/><circle cx="14" cy="15" r="2.5" fill="#fff"/></svg>+100 555 01 20</div>
    <div><svg width="28" height="18" viewBox="0 0 28 18"><rect x="1" y="1" width="26" height="16" fill="none" stroke="#111" stroke-width="2"/><path d="M1 1l13 10L27 1" fill="none" stroke="#111" stroke-width="2"/></svg>info@courtgrove.com</div>
  </div>
  <nav class="nav">
    <a class="active">Home</a><a>About Us</a><a>Services</a><a>Booking</a><a>News</a><a>Coaches</a><a>Club</a><a>Sport Store</a><a>Prices</a><a>Contact Us</a>
  </nav>
  <div class="hero" role="img" aria-label="Young players training on a clay tennis court behind a fence among green trees"></div>
  <div class="slides">
    <div class="arrow"><span><svg width="12" height="14" viewBox="0 0 12 14"><path d="M9 1L3 7l6 6" fill="none" stroke="#2e8f3a" stroke-width="3"/></svg></span></div>
    <div class="slide current">Tennis Academy</div>
    <div class="slide">Comfortable Stay</div>
    <div class="slide">Fitness &amp; Spa</div>
    <div class="slide">Horse Riding</div>
    <div class="arrow"><span><svg width="12" height="14" viewBox="0 0 12 14"><path d="M3 1l6 6-6 6" fill="none" stroke="#2e8f3a" stroke-width="3"/></svg></span></div>
  </div>
  <div class="shadow"></div>
  <h1 class="welcome">Welcome to Court Grove</h1>
  <p class="intro">Lorem ipsum dolor sit amet, consectetur adipiscing elit. Curabitur sollicitudin lectus non magna sagittis hendrerit. Vivamus interdum sagittis erat ut mattis. Pellentesque non lectus tincidunt erat imperdiet pellentesque. Sed volutpat, erat non vestibulum blandit, sapien libero porttitor magna, vitae placerat justo turpis quis nunc.</p>
  <div class="divider left"></div>
  <div class="divider right"></div>
  <div class="read-more">Read more</div>
  <div class="social"><span></span><span></span></div>
  <p class="copyright">Copyright © 2012 Court Grove. All Rights Reserved. | <a>Sitemap</a></p>
</div>
</body>
</html>
```